Velmora Medical Business Card Design

This is a private medical device company. We recently launched the new website and would like to redesign the business cards. Please see the website: www.velmoramedical.example. We'd like to keep the cards simple and professional but modern to match the website and collateral branding. Our customers are physicians and investors. I have attached the old design for comparison. I have also attached the updated logo. Please note the business card information will change, based on all employees who need to order them. So I will need to be able easily edit the copy.
Updates

Hi designers-thank you very much for submitting designs. I look forward to the results!! Joan

Target Market(s)

Our target audience are physicians

Industry/Entity Type

Medical

Contact Information for Business Card

Dorothy Wensley
Director of Marketing and Reimbursement
dwensley@velmoramedical.example
M: xxx-xxx-xxxx
O: xxx-xxx-xxxx
4120 Pinto Ridge Rd.
Suite 610
Austin, TX 78592

Font styles to use
Sans Serif

Requirements
Must have
• Must include the logo and a color or color from the logo and branding
Nice to have
• Maybe include the logo icon on the back.

```html
<!DOCTYPE html>
<html lang="en">
<head>
<meta charset="utf-8">
<title>Velmora Medical Business Cards</title>
<link href="https://fonts.googleapis.com/css2?family=Michroma&family=Montserrat:wght@300;400;500&display=swap" rel="stylesheet">
<style>
  :root{
    --canvas:#f5f6f6;
    --card:#ffffff;
    --card-dark:#2e2d2c;
    --ink:#3d3b3b;
    --ink-soft:#6b6969;
    --teal:#5a9cab;
    --teal-light:#7bb9c9;
    --red:#e0304a;
    --red-deep:#c8263d;
    --slate:#4a4645;
    --white:#ffffff;
  }
  *{box-sizing:border-box;margin:0;padding:0}
  html,body{width:1200px;height:900px;overflow:hidden;background:var(--canvas)}
  body{position:relative;font-family:"Montserrat",sans-serif;color:var(--ink)}

  .card{
    position:absolute;width:468px;height:267px;background:var(--card);
    box-shadow:2px 3px 6px rgba(0,0,0,.28);overflow:hidden;
  }
  .card--front-a{left:105px;top:155px}
  .card--back-a{left:628px;top:155px}
  .card--back-b{left:105px;top:477px}
  .card--front-b{left:628px;top:477px;background:var(--card-dark)}

  .pattern-field{position:absolute;top:0;height:267px}
  .pattern-field--right{left:237px;width:231px;
    clip-path:polygon(22% 0,100% 0,100% 100%,0 100%);
    background:linear-gradient(165deg,var(--teal) 0%,var(--teal-light) 30%,var(--red) 55%,var(--slate) 85%);}
  .pattern-field--left{left:0;width:232px;
    clip-path:polygon(0 0,100% 0,78% 100%,0 100%);
    background:linear-gradient(195deg,var(--teal) 0%,var(--red-deep) 40%,var(--red) 55%,var(--slate) 90%);}

  .wordmark{position:absolute;display:flex;align-items:center;gap:7px;
    font-family:"Montserrat",sans-serif;font-weight:500;font-size:19px;color:var(--ink);white-space:nowrap}
  .wordmark__dot{width:13px;height:13px;border-radius:50%;background:var(--teal)}
  .card--front-a .wordmark{left:37px;top:127px}
  .card--back-a .wordmark{right:32px;top:37px}
  .card--back-b .wordmark{left:22px;top:26px}
  .card--front-b .wordmark{left:288px;top:124px;color:var(--white)}

  .person{position:absolute}
  .person__name{font-family:"Michroma",sans-serif;font-size:13px;color:var(--ink);letter-spacing:.1px;white-space:nowrap}
  .person__role{font-size:7.5px;color:var(--ink-soft);margin-top:2px}
  .card--back-a .person{right:32px;top:116px;text-align:right}
  .card--back-b .person{left:22px;top:160px}

  .contact{position:absolute;font-size:10px;font-weight:300;color:var(--ink);line-height:17px;list-style:none}
  .contact li{display:flex;align-items:center;gap:8px;white-space:nowrap}
  .card--back-a .contact{right:32px;top:166px;text-align:right}
  .card--back-a .contact li{justify-content:flex-end}
  .card--back-a .contact .address{line-height:15px;margin-bottom:4px}
  .card--back-b .contact{left:22px;top:204px}
  .icon{width:12px;height:12px;background:var(--teal);border-radius:1px;display:inline-flex;align-items:center;justify-content:center}
  .icon svg{width:8px;height:8px}
</style>
</head>
<body>

<section class="card card--front-a" aria-label="Card front, white">
  <div class="pattern-field pattern-field--right" role="img" aria-label="Angular brand pattern in teal, red and grey"></div>
  <div class="wordmark"><span class="wordmark__dot"></span>Velmora Medical</div>
</section>

<section class="card card--back-a" aria-label="Card back with full address">
  <div class="pattern-field pattern-field--left" role="img" aria-label="Angular brand pattern in teal, red and grey"></div>
  <div class="wordmark"><span class="wordmark__dot"></span>Velmora Medical</div>
  <div class="person">
    <p class="person__name">DOROTHY WENSLEY</p>
    <p class="person__role">Director</p>
  </div>
  <ul class="contact">
    <li class="address">4120 Pinto Ridge Road, Suite 610<br>Austin, TX 78592</li>
    <li>(512) 555-0148
      <span class="icon"><svg viewBox="0 0 8 8"><path d="M1.5 1 L3 1 L3.5 2.6 L2.6 3.2 Q3.3 4.7 4.8 5.4 L5.4 4.5 L7 5 L7 6.5 Q3.5 7 1 3 Z" fill="#fff"/></svg></span></li>
    <li>dwensley@velmoramedical.example
      <span class="icon"><svg viewBox="0 0 8 8"><rect x="0.8" y="1.8" width="6.4" height="4.4" fill="#fff"/><path d="M0.8 1.8 L4 4.4 L7.2 1.8" stroke="#5a9cab" stroke-width=".7" fill="none"/></svg></span></li>
    <li>www.velmoramedical.example
      <span class="icon"><svg viewBox="0 0 8 8"><circle cx="4" cy="4" r="3" stroke="#fff" stroke-width=".8" fill="none"/><path d="M1 4 H7 M4 1 V7" stroke="#fff" stroke-width=".7"/></svg></span></li>
  </ul>
</section>

<section class="card card--back-b" aria-label="Card back, compact layout">
  <div class="pattern-field pattern-field--right" role="img" aria-label="Angular brand pattern in teal, red and grey"></div>
  <div class="wordmark"><span class="wordmark__dot"></span>Velmora Medical</div>
  <div class="person">
    <p class="person__name">DOROTHY WENSLEY</p>
    <p class="person__role">Director</p>
  </div>
  <ul class="contact">
    <li><span class="icon"><svg viewBox="0 0 8 8"><path d="M1.5 1 L3 1 L3.5 2.6 L2.6 3.2 Q3.3 4.7 4.8 5.4 L5.4 4.5 L7 5 L7 6.5 Q3.5 7 1 3 Z" fill="#fff"/></svg></span>(512) 555-0148</li>
    <li><span class="icon"><svg viewBox="0 0 8 8"><rect x="0.8" y="1.8" width="6.4" height="4.4" fill="#fff"/><path d="M0.8 1.8 L4 4.4 L7.2 1.8" stroke="#5a9cab" stroke-width=".7" fill="none"/></svg></span>dwensley@velmoramedical.example</li>
    <li><span class="icon"><svg viewBox="0 0 8 8"><circle cx="4" cy="4" r="3" stroke="#fff" stroke-width=".8" fill="none"/><path d="M1 4 H7 M4 1 V7" stroke="#fff" stroke-width=".7"/></svg></span>www.velmoramedical.example</li>
  </ul>
</section>

<section class="card card--front-b" aria-label="Card front, dark">
  <div class="pattern-field pattern-field--left" role="img" aria-label="Angular brand pattern in teal, red and grey on dark ground"></div>
  <div class="wordmark">Velmora Medical</div>
</section>

</body>
</html>
```